Business Cards and Stationary for Studio Calmaris (Massage Therapy)
BC for Massage Therapy Studio
Professional
Corwin Palde
President/CEO
742 Fenwick Rd.
Ste. 7C
Greer, SC 48213
cpalde@studiocalmaris.example
www.studiocalmaris.example
Logo AI file

```html
<!DOCTYPE html>
<html lang="en">
<head>
<meta charset="utf-8">
<title>Studio Calmaris Stationery</title>
<link href="https://fonts.googleapis.com/css2?family=Montserrat:wght@400;600;700&display=swap" rel="stylesheet">
<style>
  :root {
    --ink: #141414;
    --paper: #ffffff;
    --gold: #f0d21a;
    --gold-deep: #c9a90c;
    --grey: #6d6d6d;
    --backdrop: #e9e6e1;
  }
  * { box-sizing: border-box; margin: 0; padding: 0; }
  html, body { width: 1200px; height: 516px; overflow: hidden; }
  body {
    background: var(--backdrop);
    font-family: "Montserrat", Arial, sans-serif;
    color: var(--ink);
    position: relative;
  }
  .piece { position: absolute; box-shadow: 0 3px 10px rgba(0,0,0,.18); overflow: hidden; }

  /* brand lockup */
  .brand { display: flex; align-items: center; gap: 6px; }
  .brand-dot { width: 16px; height: 16px; border-radius: 50%; background: var(--gold); flex: none; }
  .brand-name { font-weight: 700; font-size: 8px; letter-spacing: .08em; text-transform: uppercase; }
  .brand--dark .brand-name { color: var(--gold); }
  .brand--light .brand-name { color: var(--ink); }

  /* business cards */
  .card { width: 200px; height: 118px; background: var(--ink); color: #e8e8e8; }
  .card--front { left: 22px; top: 150px; padding: 14px; }
  .card--back { left: 22px; top: 285px; display: flex; align-items: center; justify-content: center; }
  .card-name { margin-top: 18px; font-size: 9px; font-weight: 600; color: var(--gold); }
  .card-title { font-size: 6px; color: #bdbdbd; margin-bottom: 6px; }
  .card-details { font-size: 5.5px; line-height: 1.5; color: #d6d6d6; }
  .card-mark { position: absolute; right: 14px; bottom: 14px; width: 30px; height: 30px; border-radius: 50%; background: var(--gold); }
  .card-back-circle { width: 54px; height: 54px; border-radius: 50%; background: var(--gold); }

  /* letterheads */
  .letter { width: 320px; height: 414px; background: var(--paper); padding: 26px 30px; font-size: 5.5px; line-height: 1.55; }
  .letter--one { left: 258px; top: 52px; }
  .letter--two { left: 600px; top: 52px; }
  .letter-head { display: flex; justify-content: space-between; align-items: flex-start; margin-bottom: 30px; }
  .letter-contact { font-size: 5px; color: var(--grey); text-align: right; line-height: 1.5; }
  .letter p { margin-bottom: 7px; color: #333; }
  .letter-foot { position: absolute; right: 22px; bottom: 22px; width: 22px; height: 22px; border-radius: 50%; background: var(--gold); }
  .letter-rule { position: absolute; left: 30px; right: 30px; bottom: 34px; height: 1px; background: var(--gold-deep); }

  /* envelope */
  .envelope { left: 960px; top: 120px; width: 220px; height: 250px; background: var(--paper); }
  .envelope-flap { position: absolute; inset: 0 0 auto 0; height: 110px; }
  .envelope .brand { position: absolute; left: 14px; bottom: 18px; }
  .envelope-stamp { position: absolute; right: 14px; top: 126px; width: 26px; height: 30px; border: 1px solid #cfcfcf; }

  /* compliment slip */
  .slip { left: 960px; top: 392px; width: 220px; height: 96px; background: var(--paper); }
  .slip-band { position: absolute; left: 0; top: 0; bottom: 0; width: 70px; background: var(--ink); }
  .slip-band .brand { position: absolute; left: 10px; bottom: 12px; }
  .slip-band .brand-name { font-size: 5.5px; }
  .slip-dot { position: absolute; right: 14px; bottom: 14px; width: 18px; height: 18px; border-radius: 50%; background: var(--gold); }
</style>
</head>
<body>

  <!-- business card front -->
  <section class="piece card card--front">
    <div class="brand brand--dark"><span class="brand-dot"></span><span class="brand-name">Studio Calmaris</span></div>
    <div class="card-name">Corwin Palde</div>
    <div class="card-title">President/CEO</div>
    <div class="card-details">
      742 Fenwick Rd.<br>Ste. 7C<br>Greer, SC 48213<br>
      cpalde@studiocalmaris.example<br>www.studiocalmaris.example
    </div>
    <span class="card-mark"></span>
  </section>

  <!-- business card back -->
  <section class="piece card card--back">
    <span class="card-back-circle"></span>
  </section>

  <!-- letterhead with letter -->
  <article class="piece letter letter--one">
    <header class="letter-head">
      <div class="brand brand--light"><span class="brand-dot"></span><span class="brand-name">Studio Calmaris</span></div>
      <div class="letter-contact">742 Fenwick Rd., Ste. 7C<br>Greer, SC 48213<br>cpalde@studiocalmaris.example<br>www.studiocalmaris.example</div>
    </header>
    <p>March 4, 2031</p>
    <p>Ms. Delia Marsh Okafor<br>Client Relations Lead<br>Brantwell Builders Ltd.<br>Ontario, Canada</p>
    <p>Dear Ms. Okafor,</p>
    <p>Thank you for your kind note about our new studio. We are glad to welcome you for a calm and restful visit this spring.</p>
    <p>Our therapists offer deep tissue, hot stone and relaxation sessions, each planned around your needs and comfort.</p>
    <p>Please call or write to us at any time to book your first session.</p>
    <p>Warm regards,<br><br>Corwin Palde</p>
    <span class="letter-rule"></span>
    <span class="letter-foot"></span>
  </article>

  <!-- second letterhead -->
  <article class="piece letter letter--two">
    <header class="letter-head">
      <div class="brand brand--light"><span class="brand-dot"></span><span class="brand-name">Studio Calmaris</span></div>
      <div class="letter-contact">742 Fenwick Rd., Ste. 7C<br>Greer, SC 48213<br>cpalde@studiocalmaris.example<br>www.studiocalmaris.example</div>
    </header>
    <p>Thank you for your kind note about our new studio. We are glad to welcome you for a calm and restful visit this spring.</p>
    <p>Our therapists offer deep tissue, hot stone and relaxation sessions, each planned around your needs and comfort.</p>
    <span class="letter-rule"></span>
    <span class="letter-foot"></span>
  </article>

  <!-- envelope -->
  <section class="piece envelope">
    <svg class="envelope-flap" viewBox="0 0 220 110" preserveAspectRatio="none" aria-hidden="true">
      <path d="M0 0 H220 V70 Q110 118 0 70 Z" fill="#141414"/>
      <path d="M0 70 Q110 118 220 70 V80 Q110 128 0 80 Z" fill="#f0d21a"/>
    </svg>
    <span class="envelope-stamp"></span>
    <div class="brand brand--light"><span class="brand-dot"></span><span class="brand-name">Studio Calmaris</span></div>
  </section>

  <!-- compliment slip -->
  <section class="piece slip">
    <div class="slip-band">
      <div class="brand brand--dark"><span class="brand-dot"></span><span class="brand-name">Studio Calmaris</span></div>
    </div>
    <span class="slip-dot"></span>
  </section>

</body>
</html>
```